eCard to send to Realtors (real estate, professional)

We are a title insurance company which falls under the category of financial services. We are looking for someone to design an ecard that may be emailed to Realtors. The purpose of the card is to congratulate them on their new real estate listing. This means a house or condo has just been placed onto the market for sale. We'd like it to be professional but also fun and eye catching. Our colors are black, white and maroon but we can print the logo or our esignature in b/w only. Thanks!
Target Market(s)
Real estate agents, Realtors
Industry/Entity Type
Real Estate
Requirements
Nice to have
- It would be nice to have the ability to insert the clients name into this card. It would also be nice if the card is able to be imported into Constant Contact.

```html
<!DOCTYPE html>
<html lang="en">
<head>
<meta charset="UTF-8">
<title>New Listing eCard – Harlow Title &amp; Escrow Company</title>
<link href="https://fonts.googleapis.com/css2?family=Montserrat:wght@300;400;600;700&display=swap" rel="stylesheet">
<style>
  :root {
    --backdrop: #3b3b3b;
    --maroon: #a61e23;
    --maroon-deep: #6e1014;
    --brand-maroon: #7d1418;
    --listing-green: #3aa84a;
    --ink: #111111;
    --roof-black: #0d0d0d;
    --roof-grey: #a7a9ac;
    --paper: #ffffff;
  }
  * { box-sizing: border-box; margin: 0; padding: 0; }
  html, body {
    width: 1200px;
    height: 894px;
    overflow: hidden;
    background: var(--backdrop);
    font-family: "Montserrat", Arial, sans-serif;
  }
  .ecard {
    position: absolute;
    left: 126px;
    top: 120px;
    width: 956px;
    height: 652px;
    border: 3px solid var(--ink);
    border-radius: 34px;
    overflow: hidden;
    background: var(--paper);
  }
  .ecard__hero {
    position: absolute;
    left: 0; top: 0;
    width: 100%;
    height: 460px;
    background: radial-gradient(ellipse at 50% 45%, #b8252a 0%, var(--maroon) 45%, var(--maroon-deep) 100%);
    text-align: center;
  }
  .hero__headline {
    position: absolute;
    top: 22px; left: 0; width: 100%;
    font-weight: 700;
    font-size: 75px;
    line-height: 1;
    color: var(--paper);
  }
  .hero__subline {
    position: absolute;
    top: 100px; left: 0; width: 100%;
    font-weight: 400;
    font-size: 46px;
    line-height: 1;
    color: var(--listing-green);
  }
  .hero__roof {
    position: absolute;
    left: 90px; top: 163px;
    width: 769px; height: 140px;
    border-radius: 70px 70px 6px 6px;
    background: linear-gradient(90deg, var(--roof-black) 0%, #2a2a2a 40%, #6f7073 52%, var(--roof-grey) 64%, var(--roof-grey) 100%);
  }
  .hero__houses {
    position: absolute;
    left: 72px; top: 324px;
    width: 812px; height: 71px;
    border-radius: 8px;
    background: linear-gradient(90deg, #8cab3a, #e04a35, #5b8fd0, #d9a55a, #7cc3e4, #f2b01e, #8cab3a, #5b8fd0, #f08a8a, #ee6a2c);
    opacity: 0.9;
  }
  .hero__tagline {
    position: absolute;
    top: 410px; left: 0; width: 100%;
    font-weight: 700;
    font-size: 29px;
    line-height: 1.2;
    color: var(--listing-green);
  }
  .ecard__footer {
    position: absolute;
    left: 0; top: 460px;
    width: 100%; height: 192px;
  }
  .brand {
    position: absolute;
    left: 52px; top: 64px;
    display: flex;
    align-items: center;
    gap: 12px;
  }
  .brand__mark {
    width: 24px; height: 24px;
    background: var(--brand-maroon);
  }
  .brand__name {
    font-weight: 700;
    font-size: 26px;
    line-height: 1.15;
    color: var(--brand-maroon);
    text-transform: uppercase;
  }
  .contact {
    position: absolute;
    left: 430px; top: 62px;
    width: 474px;
    text-align: center;
  }
  .contact__phone {
    font-weight: 300;
    font-size: 65px;
    line-height: 1;
    color: var(--ink);
  }
  .contact__web {
    margin-top: 12px;
    font-weight: 400;
    font-size: 30px;
    line-height: 1;
    letter-spacing: 6px;
    color: var(--ink);
  }
  .contact__web strong {
    font-weight: 700;
    color: var(--brand-maroon);
  }
</style>
</head>
<body>
  <article class="ecard">
    <section class="ecard__hero">
      <h1 class="hero__headline">Congratulations</h1>
      <p class="hero__subline">on your new real estate listing</p>
      <div class="hero__roof" role="img" aria-label="Illustration of a large house roofline in black and grey"></div>
      <div class="hero__houses" role="img" aria-label="Row of ten small colourful house illustrations"></div>
      <p class="hero__tagline">A successful closing starts with a solid foundation ...</p>
    </section>
    <footer class="ecard__footer">
      <div class="brand">
        <span class="brand__mark"></span>
        <span class="brand__name">Harlow Title<br>&amp; Escrow Company</span>
      </div>
      <div class="contact">
        <p class="contact__phone">(555) 014 2278</p>
        <p class="contact__web">www.<strong>harlowtitle</strong>.com</p>
      </div>
    </footer>
  </article>
</body>
</html>
```